6 - 8 'Holistic' Instagram Graphics

Hi there!
We are looking to build up a library of Graphic Templates to use as Instagram & Facebook posts for our Holistic Medi Spa (& 3 other companies eventually)
This competition is for a sample of 6 - 8 designs. For the winner(s), we will make an agreement for a batch order (Looking for 200+ designs in total), and will be looking to make a long term arrangement.
Please find a full job description in the attached Word Document.
Any questions, don't hesitate to ask.
Thanks!
Medical Spa

```html
<!DOCTYPE html>
<html lang="en">
<head>
<meta charset="utf-8">
<title>Willowmere – profile grid</title>
<link href="https://fonts.googleapis.com/css2?family=Cormorant+Garamond:wght@300;400&family=Open+Sans:wght@400;600&family=Roboto:wght@400;500;700&display=swap" rel="stylesheet">
<style>
  :root {
    --ink: #222222;
    --muted: #8e8e8e;
    --rule: #dbdbdb;
    --bar: #f8f8f8;
    --blue: #5395e8;
    --link: #1d3a6e;
    --mint: #e4f1ee;
    --mint-deep: #cfe6e0;
    --gold: #8d8252;
    --alert: #e0565b;
  }
  * { box-sizing: border-box; margin: 0; padding: 0; }
  html, body { width: 675px; height: 1200px; overflow: hidden; background: #fff; }
  .screen { position: relative; width: 675px; height: 1200px; overflow: hidden; font-family: "Roboto", Arial, sans-serif; color: var(--ink); background: #fff; }

  .status-bar { position: absolute; top: 0; left: 0; width: 100%; height: 36px; background: var(--bar); font-size: 19px; }
  .status-bar .carrier { position: absolute; left: 12px; top: 7px; }
  .status-bar .time { position: absolute; left: 0; width: 100%; text-align: center; top: 7px; font-weight: 500; }
  .status-bar .wifi { position: absolute; left: 186px; top: 9px; }
  .status-bar .battery { position: absolute; right: 12px; top: 10px; }

  .nav-bar { position: absolute; top: 36px; left: 0; width: 100%; height: 79px; background: var(--bar); border-bottom: 1px solid var(--rule); }
  .nav-bar .title { position: absolute; width: 100%; text-align: center; top: 22px; font-size: 28px; font-weight: 700; }
  .nav-bar .add-user { position: absolute; left: 16px; top: 24px; }
  .nav-bar .settings { position: absolute; right: 15px; top: 20px; }

  .avatar { position: absolute; left: 13px; top: 128px; width: 154px; height: 154px; border-radius: 50%; background: conic-gradient(#f4b52e, #e23c63, #c22b7b, #e23c63, #f4b52e); }
  .avatar::after { content: ""; position: absolute; inset: 6px; border-radius: 50%; background: #fff; }
  .avatar .photo { position: absolute; inset: 10px; border-radius: 50%; background: #2a2a2c; z-index: 1; }

  .stats { position: absolute; top: 138px; left: 202px; width: 450px; display: flex; }
  .stat { width: 150px; text-align: center; }
  .stat b { display: block; font-size: 28px; font-weight: 700; }
  .stat span { display: block; font-size: 20px; color: var(--muted); margin-top: -2px; }

  .follow { position: absolute; left: 202px; top: 211px; width: 384px; height: 49px; background: var(--blue); color: #fff; border-radius: 4px; text-align: center; line-height: 49px; font-size: 24px; font-weight: 700; }
  .more { position: absolute; left: 594px; top: 211px; width: 57px; height: 49px; background: var(--blue); border-radius: 4px; }

  .bio { position: absolute; left: 22px; top: 298px; width: 630px; font-family: "Open Sans", Arial, sans-serif; font-size: 19.5px; line-height: 33px; }
  .site { position: absolute; left: 22px; top: 364px; font-size: 23px; color: var(--link); }

  .tabs { position: absolute; top: 430px; left: 0; width: 100%; height: 77px; border-top: 1px solid var(--rule); }
  .tabs svg { position: absolute; top: 23px; }

  .grid { position: absolute; top: 507px; left: 0; width: 675px; height: 614px; background: #fff; overflow: hidden; }
  .post { position: absolute; width: 224px; height: 225px; background: linear-gradient(135deg, var(--mint) 0%, #f3f8f6 55%, var(--mint-deep) 100%); overflow: hidden; }
  .post .photo { position: absolute; }
  .post .line { position: absolute; font-family: "Cormorant Garamond", Georgia, serif; font-weight: 300; color: var(--gold); font-size: 19px; line-height: 21px; letter-spacing: -0.3px; white-space: nowrap; }

  .bottom-bar { position: absolute; left: 0; top: 1121px; width: 100%; height: 79px; background: var(--bar); border-top: 1px solid var(--rule); }
  .bottom-bar svg { position: absolute; top: 20px; }
  .bottom-bar .dot { position: absolute; left: 469px; top: 70px; width: 6px; height: 6px; border-radius: 50%; background: var(--alert); }

  .activity { position: absolute; left: 396px; top: 1033px; width: 154px; height: 65px; background: var(--alert); border-radius: 8px; color: #fff; font-size: 27px; }
  .activity::after { content: ""; position: absolute; left: 62px; bottom: -12px; border: 13px solid transparent; border-top-color: var(--alert); border-bottom: 0; }
  .activity svg { position: absolute; top: 20px; }
  .activity span { position: absolute; top: 16px; }
</style>
</head>
<body>
<div class="screen">

  <header class="status-bar">
    <span class="carrier">●●●●● Company</span>
    <svg class="wifi" width="24" height="18" viewBox="0 0 24 18"><path d="M12 17l3-3.5a4.5 4.5 0 0 0-6 0z M5 10a10 10 0 0 1 14 0l-2 2.3a7 7 0 0 0-10 0z M1 5.5a16 16 0 0 1 22 0l-2 2.3a13 13 0 0 0-18 0z" fill="#222"/></svg>
    <span class="time">17:30</span>
    <svg class="battery" width="44" height="18" viewBox="0 0 44 18"><rect x="0.5" y="0.5" width="39" height="17" rx="3" fill="none" stroke="#222"/><rect x="2.5" y="2.5" width="35" height="13" rx="1.5" fill="#222"/><rect x="40.5" y="6" width="2.5" height="6" fill="#222"/></svg>
  </header>

  <nav class="nav-bar">
    <svg class="add-user" width="46" height="32" viewBox="0 0 46 32"><circle cx="30" cy="9" r="8" fill="#222"/><path d="M15 31c0-9 7-13 15-13s15 4 15 13z" fill="#222"/><rect x="0" y="14" width="16" height="3.5" fill="#222"/><rect x="6.2" y="8" width="3.5" height="16" fill="#222"/></svg>
    <div class="title">Willowmere</div>
    <svg class="settings" width="40" height="40" viewBox="0 0 40 40"><circle cx="20" cy="20" r="13" fill="none" stroke="#222" stroke-width="4"/><g stroke="#222" stroke-width="5"><path d="M20 1v7M20 32v7M1 20h7M32 20h7M6.5 6.5l5 5M28.5 28.5l5 5M6.5 33.5l5-5M28.5 11.5l5-5"/></g></svg>
  </nav>

  <div class="avatar"><div class="photo" role="img" aria-label="Profile photo"></div></div>

  <section class="stats">
    <div class="stat"><b>3.959</b><span>posts</span></div>
    <div class="stat"><b>8.936</b><span>followers</span></div>
    <div class="stat"><b>443</b><span>followings</span></div>
  </section>
  <div class="follow">Follow</div>
  <div class="more"><svg width="57" height="49" viewBox="0 0 57 49"><path d="M22 21h13l-6.5 7z" fill="#fff"/></svg></div>

  <p class="bio">At Willowmere, we have the most advanced treatments available to help keep you forever young &amp; beautiful!</p>
  <div class="site">Willowmere.com</div>

  <div class="tabs">
    <svg style="left:96px" width="30" height="30" viewBox="0 0 30 30" fill="#5395e8"><rect x="0" y="0" width="5" height="5"/><rect x="12.5" y="0" width="5" height="5"/><rect x="25" y="0" width="5" height="5"/><rect x="0" y="12.5" width="5" height="5"/><rect x="12.5" y="12.5" width="5" height="5"/><rect x="25" y="12.5" width="5" height="5"/><rect x="0" y="25" width="5" height="5"/><rect x="12.5" y="25" width="5" height="5"/><rect x="25" y="25" width="5" height="5"/></svg>
    <svg style="left:320px" width="36" height="30" viewBox="0 0 36 30" fill="#777"><rect x="0" y="0" width="4" height="2"/><rect x="8" y="0" width="28" height="2"/><rect x="0" y="14" width="4" height="2"/><rect x="8" y="14" width="28" height="2"/><rect x="0" y="28" width="4" height="2"/><rect x="8" y="28" width="28" height="2"/></svg>
    <svg style="left:542px;top:19px" width="40" height="36" viewBox="0 0 40 36"><path d="M2 6h12l3-4h6l3 4h12v28H2z" fill="none" stroke="#777" stroke-width="2"/><circle cx="20" cy="17" r="4" fill="none" stroke="#777" stroke-width="2"/><path d="M12 29c1-5 4-7 8-7s7 2 8 7" fill="none" stroke="#777" stroke-width="2"/></svg>
  </div>

  <main class="grid">
    <article class="post" style="left:0;top:0">
      <div class="photo" role="img" aria-label="Spa still life with candle, towel and reed diffuser" style="left:82px;top:24px;width:128px;height:180px;background:linear-gradient(160deg,#bfe0e3,#9ccfd6)"></div>
      <div class="line" style="left:18px;top:82px">Touch the body<br>Heal the mind<br>Calm the spirit</div>
    </article>
    <article class="post" style="left:226px;top:0">
      <div class="photo" role="img" aria-label="Smiling mature woman resting her chin on her hands" style="left:11px;top:23px;width:198px;height:128px;background:linear-gradient(120deg,#e9e6dc,#c9b49a 55%,#e6ece8)"></div>
      <div class="line" style="left:0;width:224px;text-align:center;top:157px">Tips for aging<br>gracefully →</div>
    </article>
    <article class="post" style="left:451px;top:0">
      <div class="photo" role="img" aria-label="Hands massaging a woman's neck during facial" style="left:8px;top:22px;width:125px;height:183px;background:linear-gradient(150deg,#b7b1ab,#d9c2b1 50%,#8e8782)"></div>
      <div class="line" style="right:14px;top:82px;text-align:right">When did you<br>last consider<br>your skincare?<br>⟶</div>
    </article>

    <article class="post" style="left:0;top:227px">
      <div class="photo" role="img" aria-label="Laser hair removal treatment on a leg" style="left:49px;top:31px;width:160px;height:101px;background:linear-gradient(120deg,#e7cfc0,#a9a9a9 60%,#e9ecef)"></div>
      <div class="line" style="left:12px;top:62px;font-size:118px;line-height:118px;letter-spacing:-4px">25%</div>
      <div class="line" style="left:26px;top:180px;font-size:17px">for all hair removal procedures</div>
    </article>
    <article class="post" style="left:226px;top:227px">
      <div class="photo" role="img" aria-label="Back massage treatment" style="left:50px;top:25px;width:107px;height:158px;background:linear-gradient(170deg,#c8d2d6,#d8b9a5 60%,#9eb3ba)"></div>
      <div class="line" style="left:20px;top:26px;font-size:44px;line-height:46px;letter-spacing:-1px">GIVEAWAY</div>
      <div class="line" style="left:172px;top:118px;font-size:24px">↓</div>
      <div class="line" style="left:56px;top:158px;font-size:12px;color:#eef3f2">see in description</div>
    </article>
    <article class="post" style="left:451px;top:227px">
      <div class="photo" role="img" aria-label="Woman receiving a facial device treatment" style="left:9px;top:25px;width:171px;height:112px;background:linear-gradient(120deg,#7fb4b8,#d8c2b4 55%,#9fc6c9)"></div>
      <div class="line" style="left:0;width:190px;text-align:center;top:148px">EMS Body<br>Sculping is equivalent<br>to 16 weeks HIIT</div>
      <div class="line" style="left:192px;top:190px">⟶</div>
    </article>

    <article class="post" style="left:0;top:454px">
      <div class="photo" role="img" aria-label="Man with hand on head, concerned about hair loss" style="left:51px;top:18px;width:162px;height:90px;background:linear-gradient(120deg,#bfc7c6,#8a7466 50%,#d7dbd9)"></div>
      <div class="line" style="left:60px;top:116px">Hair Loss &nbsp;&nbsp;Alopecia</div>
      <div class="line" style="left:0;width:265px;text-align:center;top:139px;font-size:12px;line-height:14px">Hair loss can occur for a<br>number of reasons</div>
    </article>
    <article class="post" style="left:226px;top:454px">
      <div class="line" style="left:0;width:224px;text-align:center;top:14px">Plasma Fibroblast<br>Benefits⟶</div>
      <div class="photo" role="img" aria-label="Face showing plasma fibroblast treatment zones" style="left:52px;top:69px;width:172px;height:160px;background:linear-gradient(120deg,#efe0d5,#d6b8a6 60%,#e8d6ca)"></div>
    </article>
    <article class="post" style="left:451px;top:454px">
      <div class="photo" role="img" aria-label="Woman with acne-prone skin" style="left:30px;top:11px;width:164px;height:97px;background:linear-gradient(120deg,#bcd3dc,#d9b9a6 55%,#c4d7de)"></div>
      <div class="line" style="left:0;width:224px;text-align:center;top:114px">Does acne get in<br>the way of your<br>confidence ever</div>
    </article>
  </main>

  <div class="activity">
    <svg style="left:16px" width="28" height="25" viewBox="0 0 28 25"><path d="M14 25L2.5 13.5a7 7 0 0 1 11.5-9 7 7 0 0 1 11.5 9z" fill="#fff"/></svg>
    <span style="left:54px">1</span>
    <svg style="left:90px;top:18px" width="26" height="27" viewBox="0 0 26 27"><circle cx="13" cy="7" r="6.5" fill="#fff"/><path d="M0 27c0-8 6-12 13-12s13 4 13 12z" fill="#fff"/></svg>
    <span style="left:128px">1</span>
  </div>

  <footer class="bottom-bar">
    <svg style="left:46px" width="40" height="38" viewBox="0 0 40 38"><path d="M3 17L20 2l17 15v19H26V24H14v12H3z" fill="none" stroke="#777" stroke-width="2"/></svg>
    <svg style="left:183px" width="40" height="40" viewBox="0 0 40 40"><circle cx="16" cy="16" r="13" fill="none" stroke="#777" stroke-width="2"/><path d="M26 26l12 12" stroke="#777" stroke-width="2.5"/></svg>
    <svg style="left:316px" width="42" height="42" viewBox="0 0 42 42"><rect x="1" y="1" width="40" height="40" rx="9" fill="none" stroke="#222" stroke-width="2"/><path d="M21 11v20M11 21h20" stroke="#222" stroke-width="2"/></svg>
    <svg style="left:452px;top:24px" width="40" height="34" viewBox="0 0 40 34"><path d="M20 32L4 17a9.5 9.5 0 0 1 16-11 9.5 9.5 0 0 1 16 11z" fill="none" stroke="#777" stroke-width="2"/></svg>
    <span class="dot"></span>
    <svg style="left:586px" width="40" height="40" viewBox="0 0 40 40"><circle cx="20" cy="10" r="9" fill="#222"/><path d="M1 40c0-12 8-18 19-18s19 6 19 18z" fill="#222"/></svg>
  </footer>

</div>
</body>
</html>
```